Harbor Mists - Vape Company needs product info cards

Need product info cards for the different flavors to be displayed with the bottles and to send to potential customers. Looking for the size to be 3" x 5" and 2 sided, but open to ideas. My clients logo and pictures of the sample bottles are attached. They would like the design to have a similar feel, but again are open to ideas.
Bottle 1: 7-ROX: A smooth blend of fresh cranberries, crisp apple and pomegranate that's sure to keep you wanting more
Target Market(s)
Retail
Industry/Entity Type
It Company
Colors
Designer to choose colors to be used in the design.
Look and feel
Each slider illustrates characteristics of the customer's brand and the style your logo design should communicate.

```html
<!DOCTYPE html>
<html lang="en">
<head>
<meta charset="utf-8">
<title>Harbor Mists – Product Info Cards</title>
<link href="https://fonts.googleapis.com/css2?family=Oswald:wght@500&family=Roboto+Slab:wght@800&display=swap" rel="stylesheet">
<style>
  :root {
    --page: #e6e1d8;
    --olive-light: #5d6140;
    --olive-mid: #454830;
    --olive-dark: #262819;
    --olive-edge: #3f4528;
    --brown: #6a4629;
    --brown-deep: #553621;
    --brown-dark: #3e2816;
    --gold: #d9c62b;
    --red: #c8262a;
    --white: #f4f0e6;
    --bottle-light: #7a7c45;
    --bottle-dark: #1c1c14;
  }
  html, body {
    margin: 0;
    width: 1200px;
    height: 917px;
    overflow: hidden;
    background: var(--page);
  }
  .canvas { position: relative; width: 1200px; height: 917px; }
  .card {
    position: absolute;
    top: 80px;
    width: 489px;
    height: 756px;
    overflow: hidden;
    background: radial-gradient(ellipse at 50% 40%, var(--olive-light) 0%, var(--olive-mid) 55%, var(--olive-dark) 100%);
    box-shadow: 0 3px 10px rgba(0,0,0,.35);
  }
  .card--front { left: 84px; }
  .card--back { left: 628px; }

  .brand {
    position: absolute;
    top: 150px;
    left: 0;
    width: 100%;
    display: flex;
    justify-content: center;
    align-items: center;
    gap: 10px;
    font-family: "Roboto Slab", serif;
    font-weight: 800;
    font-size: 36px;
    color: var(--gold);
    letter-spacing: 1px;
  }
  .brand__mark { width: 16px; height: 16px; background: var(--gold); }

  .contacts {
    position: absolute;
    top: 327px;
    left: 0;
    width: 100%;
    text-align: center;
    font-family: "Roboto Slab", serif;
    font-weight: 800;
    font-size: 21px;
    line-height: 33.5px;
    color: var(--gold);
  }
  .contacts span { border-bottom: 2px solid var(--gold); }

  .panel { position: absolute; left: 0; top: 0; }

  .flavor {
    position: absolute;
    left: 0;
    width: 100%;
    text-align: center;
    font-family: "Oswald", sans-serif;
    font-weight: 500;
    text-transform: uppercase;
    color: var(--white);
    font-size: 17px;
    line-height: 23.5px;
  }
  .flavor__name { font-size: 27px; line-height: 32px; }
  .flavor--rox { top: 466px; }
  .flavor--rox .flavor__name { color: var(--gold); }
  .flavor--tide { top: 626px; }
  .flavor--tide .flavor__name { color: var(--red); }

  .bottle {
    position: absolute;
    border-radius: 18px 18px 6px 6px;
    background: linear-gradient(to bottom, var(--bottle-dark) 0%, var(--bottle-dark) 28%, var(--bottle-light) 45%, #4a4a2c 100%);
  }
  .bottle--right { left: 420px; top: 404px; width: 52px; height: 208px; }
  .bottle--left { left: 18px; top: 536px; width: 50px; height: 208px; }

  .floor {
    position: absolute; left: 0; bottom: 0; width: 100%; height: 116px;
    background: linear-gradient(to bottom, #4b3821, var(--brown));
  }
  .lineup .bottle {
    border-radius: 30px 30px 8px 8px;
    background: linear-gradient(to bottom, var(--bottle-dark) 0%, var(--bottle-dark) 32%, #3a3a24 40%, var(--bottle-light) 60%, #53502e 100%);
    box-shadow: 0 4px 8px rgba(0,0,0,.4);
  }
  .lineup .b1 { left: 24px;  top: 284px; width: 104px; height: 432px; z-index: 3; }
  .lineup .b2 { left: 124px; top: 358px; width: 68px;  height: 348px; z-index: 2; }
  .lineup .b3 { left: 188px; top: 414px; width: 56px;  height: 282px; z-index: 1; }
  .lineup .b4 { left: 242px; top: 414px; width: 56px;  height: 282px; z-index: 1; }
  .lineup .b5 { left: 294px; top: 358px; width: 70px;  height: 348px; z-index: 2; }
  .lineup .b6 { left: 360px; top: 284px; width: 105px; height: 434px; z-index: 3; }
</style>
</head>
<body>
<div class="canvas">

  <section class="card card--front">
    <div class="brand"><span class="brand__mark"></span>HARBOR MISTS</div>

    <div class="contacts">
      <span>WWW.HARBORMISTS.COM</span><br>
      <span>@HARBORMISTS</span><br>
      <span>INFO@HARBORMISTS.COM</span>
    </div>

    <svg class="panel" width="489" height="756" viewBox="0 0 489 756">
      <defs>
        <linearGradient id="band" x1="0" y1="0" x2="0" y2="1">
          <stop offset="0" stop-color="var(--brown)"/>
          <stop offset="1" stop-color="var(--brown-deep)"/>
        </linearGradient>
      </defs>
      <path d="M-10 484 L140 484 L170 444 L320 444 L350 484 L499 484 V766 H-10 Z" fill="url(#band)" stroke="var(--olive-edge)" stroke-width="9" stroke-linejoin="round"/>
      <path d="M-10 644 L140 644 L170 604 L320 604 L350 644 L499 644" fill="none" stroke="var(--brown-dark)" stroke-width="7" stroke-linejoin="round"/>
    </svg>

    <div class="flavor flavor--rox">
      <div class="flavor__name">7-ROX:</div>
      A smooth blend of fresh<br>cranberries, crisp apple and<br>pomegranate that's sure to keep<br>you wanting more
    </div>

    <div class="flavor flavor--tide">
      <div class="flavor__name">HIGH TIDE:</div>
      A freshly baked, buttery crumb cake<br>infused with raspberry swirl,<br>all topped off with vanilla icing
    </div>

    <div class="bottle bottle--right" role="img" aria-label="Photo of a 7-ROX dropper bottle"></div>
    <div class="bottle bottle--left" role="img" aria-label="Photo of a High Tide dropper bottle"></div>
  </section>

  <section class="card card--back">
    <div class="brand"><span class="brand__mark"></span>HARBOR MISTS</div>
    <div class="floor"></div>
    <div class="lineup">
      <div class="bottle b1" role="img" aria-label="Photo of a large 7-ROX bottle"></div>
      <div class="bottle b2" role="img" aria-label="Photo of a medium 7-ROX bottle"></div>
      <div class="bottle b3" role="img" aria-label="Photo of a small 7-ROX bottle"></div>
      <div class="bottle b4" role="img" aria-label="Photo of a small High Tide bottle"></div>
      <div class="bottle b5" role="img" aria-label="Photo of a medium High Tide bottle"></div>
      <div class="bottle b6" role="img" aria-label="Photo of a large High Tide bottle"></div>
    </div>
  </section>

</div>
</body>
</html>
```